App Design - Job Lantern Quokka

We require an App Design for our new App called 'Lantern Quokka'. This app is essentially an assistant to help Users prepare for job interviews, to help them get hired. <br/><br/>Users who download the App can view common Questions and Answers, save their favourite responses and also view common Interview Tips. <br/><br/>The vision for our App is for Users who are preparing for an interview (1 week before, 1 day before, even 1 hour before), are able to download, view and educate themselves on common questions and responses, and then be confident to land the job. <br/><br/>Our team has developed wireframes to help highlight what each screen should do and include. Please see attached document, which also highlights key requirements for the experience. Feel free to add/remove/edit what you see on these wireframes. Our preference is that you use Adobe XD please.<br/><br/>In terms of design guidelines, we want the experience to be simple, intuitive and 'memorable' to help Users to remember the questions/responses when they are in the interview. <br/><br/>The final design should communicate 'neat and clean professionalism'; we like the design of: marlo vane com au<br/><br/>Thank you for reading! Good luck !

Target Market(s)

Professional job seekers

Font styles to use
Sans Serif

Colors

Designer to choose colors to be used in the design.

Requirements
Must have
• Please see my PlanHive_UX file that I have uploaded
Nice to have
• Could you also please include some ideas on how we can incorporate Advertising into the app screens

```html
<!DOCTYPE html>
<html lang="en">
<head>
<meta charset="utf-8">
<title>Lantern Quokka – App Screens</title>
<link href="https://fonts.googleapis.com/css2?family=Montserrat:wght@500;600;700&family=Poppins:wght@400;500;600;700&display=swap" rel="stylesheet">
<style>
  :root{
    --blue:#1f6bf0;
    --blue-dark:#1553c4;
    --blue-soft:#e7efff;
    --ink:#1d2440;
    --muted:#7d869c;
    --line:#e3e8f3;
    --bg:#ffffff;
    --screen-bg:#f4f6fb;
    --card:#ffffff;
    --danger:#ef4b5b;
  }
  *{box-sizing:border-box;margin:0;padding:0}
  html,body{width:1200px;height:2208px;overflow:hidden;background:var(--bg)}
  body{position:relative;font-family:'Poppins',sans-serif;color:var(--ink)}

  .screen{position:absolute;width:300px;height:560px;background:var(--screen-bg);
    border:2px solid var(--blue);border-radius:30px;overflow:hidden;display:flex;flex-direction:column}
  .caption{position:absolute;width:300px;text-align:center;font-family:'Montserrat',sans-serif;
    font-weight:600;font-size:13px;letter-spacing:.08em;color:var(--ink)}

  .col-1{left:80px}.col-2{left:450px}.col-3{left:820px}
  .row-1{top:40px}.row-2{top:752px}.row-3{top:1472px}
  .cap-1{top:624px}.cap-2{top:1336px}.cap-3{top:2056px}

  .topbar{height:54px;background:var(--card);display:flex;align-items:center;gap:10px;padding:0 18px;
    border-bottom:1px solid var(--line);flex-shrink:0}
  .topbar-title{font-size:12px;font-weight:600}
  .topbar svg{flex-shrink:0}
  .brand-mark{width:22px;height:22px;border-radius:6px;background:var(--blue)}
  .brand-name{font-size:12px;font-weight:600;color:var(--ink)}

  .body{flex:1;padding:14px 16px;display:flex;flex-direction:column;gap:10px;overflow:hidden}
  .card{background:var(--card);border-radius:10px;padding:12px 14px;box-shadow:0 2px 6px rgba(29,36,64,.06)}
  .card-title{font-size:11px;font-weight:600;color:var(--blue)}
  .card-text{font-size:9px;line-height:1.5;color:var(--muted);margin-top:4px}
  .card-link{display:flex;justify-content:space-between;align-items:center;font-size:9px;font-weight:600;
    color:var(--blue);margin-top:8px}
  .row-head{display:flex;justify-content:space-between;align-items:center;font-size:10px}
  .row-head .label{font-weight:600}
  .row-head .action{color:var(--blue);font-weight:500}
  .remove{color:var(--danger);font-size:9px;font-weight:500}

  /* landing */
  .landing .hero{margin:26px 22px 0;height:230px;border-radius:16px;
    background:linear-gradient(160deg,#dbe6ff 0%,#b9cffc 55%,#6f9bf5 100%)}
  .landing .intro{margin:22px 24px 0;font-size:10px;line-height:1.6;color:var(--muted)}
  .fab{position:absolute;right:20px;bottom:22px;width:40px;height:40px;border-radius:50%;background:var(--blue);
    display:flex;align-items:center;justify-content:center}

  /* menu */
  .menu .topbar{background:var(--blue);justify-content:center;border:none;height:62px}
  .menu .topbar .brand-mark{background:#fff}
  .menu-item{background:var(--card);border-radius:12px;padding:0 18px;height:108px;display:flex;
    align-items:center;justify-content:space-between;box-shadow:0 2px 6px rgba(29,36,64,.06)}
  .menu-item span{font-size:14px;font-weight:600;color:var(--blue);line-height:1.3;width:150px}

  /* categories */
  .category{background:var(--card);border-radius:10px;height:78px;display:flex;align-items:center;gap:14px;
    padding:0 14px;box-shadow:0 2px 6px rgba(29,36,64,.06)}
  .category .icon{width:34px;height:34px;border-radius:50%;background:var(--blue-soft);flex-shrink:0}
  .category span{font-size:12px;font-weight:600;color:var(--blue)}

  /* responses */
  .card.active{background:var(--blue)}
  .card.active .card-title,.card.active .card-text{color:#fff}
  .response-head{display:flex;justify-content:space-between;align-items:center}

  /* tips */
  .tip-cat{background:var(--card);border-radius:10px;padding:16px;height:112px;display:flex;flex-direction:column;
    justify-content:space-between;box-shadow:0 2px 6px rgba(29,36,64,.06)}
  .tip-cat span{font-size:14px;font-weight:600;color:var(--ink);line-height:1.3}
  .tip-cat em{font-style:normal;font-size:9px;font-weight:600;color:var(--blue)}
  .tip-detail .card-text{font-size:10px;line-height:1.7;margin-top:10px}
</style>
</head>
<body>

<!-- Landing -->
<section class="screen landing col-1 row-1">
  <div class="topbar"><div class="brand-mark"></div><div class="brand-name">Lantern Quokka</div></div>
  <div class="hero" role="img" aria-label="Illustration of a job seeker preparing for an interview"></div>
  <p class="intro">Get guided practice with common interview questions and responses so you feel ready to get hired.</p>
  <div class="fab"><svg width="16" height="16" viewBox="0 0 16 16"><path d="M3 8h10M9 4l4 4-4 4" stroke="#fff" stroke-width="2" fill="none" stroke-linecap="round" stroke-linejoin="round"/></svg></div>
</section>
<div class="caption col-1 cap-1">LANDING SCREEN</div>

<!-- Menu -->
<section class="screen menu col-2 row-1">
  <div class="topbar"><div class="brand-mark"></div></div>
  <div class="body" style="gap:14px;padding-top:18px">
    <div class="menu-item"><span>View Questions &amp; Responses</span><svg width="8" height="12" viewBox="0 0 8 12"><path d="M2 2l4 4-4 4" stroke="#1f6bf0" stroke-width="2" fill="none"/></svg></div>
    <div class="menu-item"><span>My Questions Portfolio</span><svg width="8" height="12" viewBox="0 0 8 12"><path d="M2 2l4 4-4 4" stroke="#1f6bf0" stroke-width="2" fill="none"/></svg></div>
    <div class="menu-item"><span>Interview Tips</span><svg width="8" height="12" viewBox="0 0 8 12"><path d="M2 2l4 4-4 4" stroke="#1f6bf0" stroke-width="2" fill="none"/></svg></div>
  </div>
</section>
<div class="caption col-2 cap-1">MENU SCREEN</div>

<!-- Categories -->
<section class="screen col-3 row-1">
  <div class="topbar"><svg width="10" height="14" viewBox="0 0 10 14"><path d="M8 2L3 7l5 5" stroke="#1d2440" stroke-width="2" fill="none"/></svg><div class="topbar-title">View Questions &amp; Responses</div></div>
  <div class="body">
    <div class="row-head"><span class="label">Select your category</span><span class="action">Cancel</span></div>
    <div class="category"><div class="icon"></div><span>Behavioural</span></div>
    <div class="category"><div class="icon"></div><span>Situational</span></div>
    <div class="category"><div class="icon"></div><span>Motivational</span></div>
    <div class="category"><div class="icon"></div><span>Technical</span></div>
    <div class="category"><div class="icon"></div><span>General</span></div>
  </div>
</section>
<div class="caption col-3 cap-1">VIEW QUESTIONS &amp; RESPONSES</div>

<!-- Questions -->
<section class="screen col-1 row-2">
  <div class="topbar"><svg width="10" height="14" viewBox="0 0 10 14"><path d="M8 2L3 7l5 5" stroke="#1d2440" stroke-width="2" fill="none"/></svg><div class="topbar-title">Behavioural</div></div>
  <div class="body" style="gap:14px">
    <div class="card"><div class="card-title">Question #01</div><p class="card-text">Tell us about a time you solved a difficult problem at work.</p><div class="card-link">View Answer<svg width="6" height="10" viewBox="0 0 6 10"><path d="M1 1l4 4-4 4" stroke="#1f6bf0" stroke-width="1.6" fill="none"/></svg></div></div>
    <div class="card"><div class="card-title">Question #02</div><p class="card-text">Describe a situation where you had to work closely with a team.</p><div class="card-link">View Answer<svg width="6" height="10" viewBox="0 0 6 10"><path d="M1 1l4 4-4 4" stroke="#1f6bf0" stroke-width="1.6" fill="none"/></svg></div></div>
    <div class="card"><div class="card-title">Question #03</div><p class="card-text">Give an example of a goal you set and how you reached it.</p><div class="card-link">View Answer<svg width="6" height="10" viewBox="0 0 6 10"><path d="M1 1l4 4-4 4" stroke="#1f6bf0" stroke-width="1.6" fill="none"/></svg></div></div>
  </div>
</section>
<div class="caption col-1 cap-2">VIEW QUESTIONS</div>

<!-- Responses -->
<section class="screen col-2 row-2">
  <div class="topbar"><svg width="10" height="14" viewBox="0 0 10 14"><path d="M8 2L3 7l5 5" stroke="#1d2440" stroke-width="2" fill="none"/></svg><div class="topbar-title">Responses</div></div>
  <div class="body">
    <div class="card active"><div class="card-title">Question #01</div><p class="card-text">Tell us about a time you solved a difficult problem at work.</p></div>
    <div class="card"><div class="response-head"><div class="card-title">Response #01</div><svg width="12" height="11" viewBox="0 0 12 11"><path d="M6 10L1.5 5.6A2.6 2.6 0 0 1 6 2a2.6 2.6 0 0 1 4.5 3.6z" fill="#1f6bf0"/></svg></div><p class="card-text">I broke the problem into steps, asked the team for input and tracked progress daily.</p></div>
    <div class="card"><div class="response-head"><div class="card-title">Response #02</div><svg width="12" height="11" viewBox="0 0 12 11"><path d="M6 10L1.5 5.6A2.6 2.6 0 0 1 6 2a2.6 2.6 0 0 1 4.5 3.6z" fill="none" stroke="#1f6bf0" stroke-width="1.3"/></svg></div><p class="card-text">I broke the problem into steps, asked the team for input and tracked progress daily.</p></div>
    <div class="card"><div class="response-head"><div class="card-title">Response #03</div><svg width="12" height="11" viewBox="0 0 12 11"><path d="M6 10L1.5 5.6A2.6 2.6 0 0 1 6 2a2.6 2.6 0 0 1 4.5 3.6z" fill="#1f6bf0"/></svg></div><p class="card-text">I broke the problem into steps, asked the team for input and tracked progress daily.</p></div>
  </div>
</section>
<div class="caption col-2 cap-2">VIEW QUESTION &amp; RESPONSES-2</div>

<!-- Portfolio -->
<section class="screen col-3 row-2">
  <div class="topbar"><svg width="10" height="14" viewBox="0 0 10 14"><path d="M8 2L3 7l5 5" stroke="#1d2440" stroke-width="2" fill="none"/></svg><div class="topbar-title">My Questions Portfolio</div></div>
  <div class="body" style="gap:12px">
    <p class="card-text" style="margin:0;color:var(--ink)">Find your saved answers here and review them before your next interview.</p>
    <div class="card"><div class="row-head"><span class="card-title">Question #01</span><span class="remove">Remove</span></div><p class="card-text" style="color:var(--ink);font-weight:500">What are your greatest strengths?</p><div style="height:52px"></div></div>
    <div class="card"><div class="row-head"><span class="card-title">Question #02</span><span class="remove">Remove</span></div><p class="card-text" style="color:var(--ink);font-weight:500">What are your greatest strengths?</p><div style="height:52px"></div></div>
    <div class="card"><div class="row-head"><span class="card-title">Question #03</span><span class="remove">Remove</span></div><p class="card-text" style="color:var(--ink);font-weight:500">What are your greatest strengths?</p><div style="height:52px"></div></div>
  </div>
</section>
<div class="caption col-3 cap-2">VIEW 'MY QUESTION PORTFOLIO'</div>

<!-- Tip categories -->
<section class="screen col-1 row-3">
  <div class="topbar"><svg width="10" height="14" viewBox="0 0 10 14"><path d="M8 2L3 7l5 5" stroke="#1d2440" stroke-width="2" fill="none"/></svg><div class="topbar-title">View Interview Tips</div></div>
  <div class="body" style="gap:14px">
    <div class="row-head"><span class="label">Select your tip category</span><span class="action">Cancel</span></div>
    <div class="tip-cat"><span>Tips for before<br>the interview</span><em>View tip</em></div>
    <div class="tip-cat"><span>Tips for during<br>the interview</span><em>View tip</em></div>
    <div class="tip-cat"><span>Tips for after<br>the interview</span><em>View tip</em></div>
  </div>
</section>
<div class="caption col-1 cap-3">VIEW INTERVIEW TIPS</div>

<!-- Tips list -->
<section class="screen col-2 row-3">
  <div class="topbar"><svg width="10" height="14" viewBox="0 0 10 14"><path d="M8 2L3 7l5 5" stroke="#1d2440" stroke-width="2" fill="none"/></svg><div class="topbar-title">View Interview Tips</div></div>
  <div class="body">
    <div class="card"><div class="card-title">Tip #01</div><p class="card-text">Research the company and the role before you arrive.</p><div class="card-link">View More<svg width="6" height="10" viewBox="0 0 6 10"><path d="M1 1l4 4-4 4" stroke="#1f6bf0" stroke-width="1.6" fill="none"/></svg></div></div>
    <div class="card"><div class="card-title">Tip #02</div><p class="card-text">Research the company and the role before you arrive.</p><div class="card-link">View More<svg width="6" height="10" viewBox="0 0 6 10"><path d="M1 1l4 4-4 4" stroke="#1f6bf0" stroke-width="1.6" fill="none"/></svg></div></div>
    <div class="card"><div class="card-title">Tip #03</div><p class="card-text">Research the company and the role before you arrive.</p><div class="card-link">View More<svg width="6" height="10" viewBox="0 0 6 10"><path d="M1 1l4 4-4 4" stroke="#1f6bf0" stroke-width="1.6" fill="none"/></svg></div></div>
    <div class="card"><div class="card-title">Tip #04</div><p class="card-text">Research the company and the role before you arrive.</p><div class="card-link">View More<svg width="6" height="10" viewBox="0 0 6 10"><path d="M1 1l4 4-4 4" stroke="#1f6bf0" stroke-width="1.6" fill="none"/></svg></div></div>
    <div class="card"><div class="card-title">Tip #05</div><p class="card-text">Research the company and the role before you arrive.</p><div class="card-link">View More<svg width="6" height="10" viewBox="0 0 6 10"><path d="M1 1l4 4-4 4" stroke="#1f6bf0" stroke-width="1.6" fill="none"/></svg></div></div>
  </div>
</section>
<div class="caption col-2 cap-3">VIEW INTERVIEW TIPS-2</div>

<!-- Tip detail -->
<section class="screen tip-detail col-3 row-3">
  <div class="topbar"><svg width="10" height="14" viewBox="0 0 10 14"><path d="M8 2L3 7l5 5" stroke="#1d2440" stroke-width="2" fill="none"/></svg><div class="topbar-title">View Interview Tips</div></div>
  <div class="body">
    <div class="card" style="padding:16px"><div class="card-title">Tip #01</div><p class="card-text">Arrive ten minutes early, dress a step above the office standard and bring a printed copy of your resume.</p><p class="card-text">Take a moment to breathe, smile when you meet the panel and listen closely to each question before you answer.</p><p class="card-text">Keep your responses clear, specific and focused on results.</p><div style="height:150px"></div></div>
  </div>
</section>
<div class="caption col-3 cap-3">VIEW INTERVIEW TIPS-3</div>

</body>
</html>
```